Veltrano Energy Business Card Design

website: www.veltranoenergy.example
Project: Business Card Design for Veltrano Energy
Name: Dorian Kettle
Title: Founder / Operations Strategist
Visual Identity & Logo:
Logo File: VEL-Logo-FullGradient-Final.png (Attached).
Color Palette: The brand relies on a distinctive Cyan (Blue) to Lime Green gradient.
Background Preference: We want a Dark Mode aesthetic (Deep Matte Black, Charcoal, or Dark Slate) to make the neon gradient of the logo pop. This feels more "tech/industrial" than a standard white card.
Design Aesthetic (The "Ops" Vibe):
Concept: "Grid & Infrastructure." We are a solar rental company, focusing on logistics and access.
Typography: White, bold sans-serif text for contact info. High contrast against the dark background.
Accents: Use the Cyan or Lime Green from the logo for thin divider lines or edge painting.
Avoid: No orange/gold (clashes with logo). No cartoon leaves.
Layout Requirements:
Front: Large, centered logo. Maybe a subtle UV gloss spot varnish over the logo icon.
Back: Name, Title, Contact Info.
Texture: Matte finish cardstock with gloss elements.
sample mock up of information on card: https://brivomarkco-my.filehost.example/:i:/g/personal/dorian_kettle_veltranoenergy_example/AbCdEfGhIjKlMnOpQrStUvWxYz012345678?e=Xy12Ab
Logo: https://brivomarkco.filehost.example/:i:/s/VeltranoEnergy/ZyXwVuTsRqPoNmLkJiHgFeDcBa9876543210?e=Pq34Cd

```html
<!DOCTYPE html>
<html lang="en">
<head>
<meta charset="utf-8">
<title>Veltrano Energy Business Card</title>
<link rel="stylesheet" href="https://fonts.googleapis.com/css2?family=Poppins:wght@400;500;600;700&display=swap">
<style>
  :root {
    --page: #ffffff;
    --card: #08090a;
    --ink: #ffffff;
    --cyan: #1aa3d8;
    --teal: #22b8c8;
    --lime: #9ccc5a;
    --shadow: rgba(0, 0, 0, 0.28);
  }
  * { margin: 0; padding: 0; box-sizing: border-box; }
  html, body {
    width: 989px;
    height: 1200px;
    overflow: hidden;
    background: var(--page);
    font-family: "Poppins", sans-serif;
    color: var(--ink);
  }
  .sheet { position: relative; width: 989px; height: 1200px; }
  .card {
    position: absolute;
    left: 156px;
    width: 679px;
    height: 387px;
    background: var(--card);
    border-radius: 18px;
    box-shadow: 14px 16px 26px var(--shadow);
    overflow: hidden;
  }
  .card--contact { top: 158px; }
  .card--brand { top: 645px; }

  /* contact side */
  .brand-mark {
    position: absolute;
    left: 82px;
    top: 130px;
    width: 200px;
    display: flex;
    align-items: center;
    gap: 12px;
  }
  .brand-mark__square {
    width: 22px; height: 22px;
    background: var(--teal);
    flex: none;
  }
  .brand-mark__name {
    font-weight: 500;
    font-size: 28px;
    line-height: 1.1;
    color: var(--teal);
  }
  .person {
    position: absolute;
    left: 364px;
    top: 92px;
  }
  .person__name {
    font-weight: 600;
    font-size: 33px;
    line-height: 1.2;
    letter-spacing: 0.2px;
  }
  .person__title {
    margin-top: 6px;
    font-weight: 500;
    font-size: 15px;
    letter-spacing: 0.1px;
  }
  .accent-bar {
    position: absolute;
    left: 316px;
    top: 216px;
    width: 37px;
    height: 171px;
    border-radius: 18px 18px 0 0;
    background: linear-gradient(180deg, var(--cyan) 0%, var(--teal) 40%, var(--lime) 100%);
  }
  .contact-list {
    position: absolute;
    left: 316px;
    top: 238px;
    list-style: none;
  }
  .contact-list__item {
    display: flex;
    align-items: flex-start;
    height: 36px;
    font-size: 19px;
    font-weight: 400;
    line-height: 25px;
  }
  .contact-list__item--address { height: auto; }
  .contact-list__icon {
    width: 37px;
    height: 25px;
    display: flex;
    align-items: center;
    justify-content: center;
    flex: none;
  }
  .contact-list__icon svg { width: 15px; height: 15px; fill: var(--card); }
  .contact-list__text { margin-left: 11px; }

  /* brand side */
  .lockup {
    position: absolute;
    left: 0; right: 0;
    top: 148px;
    display: flex;
    justify-content: center;
    align-items: center;
    gap: 16px;
  }
  .lockup__square {
    width: 34px; height: 34px;
    background: var(--teal);
  }
  .lockup__name {
    font-weight: 400;
    font-size: 48px;
    line-height: 1;
    color: var(--teal);
    letter-spacing: 0.5px;
  }
  .tagline {
    position: absolute;
    left: 0; right: 0;
    top: 316px;
    text-align: center;
    font-weight: 600;
    font-size: 14px;
    letter-spacing: 1.2px;
  }
</style>
</head>
<body>
<main class="sheet">
  <section class="card card--contact" aria-label="Contact side">
    <div class="brand-mark">
      <span class="brand-mark__square"></span>
      <span class="brand-mark__name">Veltrano Energy</span>
    </div>
    <div class="person">
      <h1 class="person__name">Dorian Kettle</h1>
      <p class="person__title">Founder / Operations Strategist</p>
    </div>
    <div class="accent-bar"></div>
    <ul class="contact-list">
      <li class="contact-list__item">
        <span class="contact-list__icon"><svg viewBox="0 0 24 24" aria-hidden="true"><path d="M6.6 10.8a15.1 15.1 0 0 0 6.6 6.6l2.2-2.2a1 1 0 0 1 1-.25 11.4 11.4 0 0 0 3.6.57 1 1 0 0 1 1 1V20a1 1 0 0 1-1 1A17 17 0 0 1 3 4a1 1 0 0 1 1-1h3.5a1 1 0 0 1 1 1c0 1.25.2 2.45.57 3.57a1 1 0 0 1-.25 1z"/></svg></span>
        <span class="contact-list__text">555-014-2270</span>
      </li>
      <li class="contact-list__item">
        <span class="contact-list__icon"><svg viewBox="0 0 24 24" aria-hidden="true"><path d="M4 3l16 7-6.5 2L20 18.5 18.5 20 12 13.5 10 20z"/></svg></span>
        <span class="contact-list__text">www.veltranoenergy.example</span>
      </li>
      <li class="contact-list__item contact-list__item--address">
        <span class="contact-list__icon"><svg viewBox="0 0 24 24" aria-hidden="true"><path d="M12 2a7 7 0 0 0-7 7c0 5.2 7 13 7 13s7-7.8 7-13a7 7 0 0 0-7-7zm0 9.5A2.5 2.5 0 1 1 12 6.5a2.5 2.5 0 0 1 0 5z"/></svg></span>
        <span class="contact-list__text">4120 Marrow Creek Lane<br>Orlando, FL 32811</span>
      </li>
    </ul>
  </section>

  <section class="card card--brand" aria-label="Brand side">
    <div class="lockup">
      <span class="lockup__square"></span>
      <span class="lockup__name">Veltrano Energy</span>
    </div>
    <p class="tagline">No Debt, No Liens, No Maintenance, Just Savings.</p>
  </section>
</main>
</body>
</html>
```